App Design for a petrol price in Nigeria

Through your already existing prototypes, we intend to design an app that would show petrol prices in Nigeria. The app would enable the user monitor the prices of petrol products in real time from nearby stations.

Industry/Entity Type

Gas And Oil

Requirements
Must have
• User community (sign up) and crowdsourced database integration

```html
<!DOCTYPE html>
<html lang="en">
<head>
<meta charset="utf-8">
<title>Update Data – Crowdsourced Price Form</title>
<link href="https://fonts.googleapis.com/css2?family=Mulish:wght@400;600;700&family=Poppins:wght@500;700&display=swap" rel="stylesheet">
<style>
  :root {
    --page-bg: #f7f7fc;
    --brand-green: #33a061;
    --headline-green: #2e9e5b;
    --circle-tint: #f1f5f4;
    --circle-tint-dark: #36a365;
    --ink: #2d3340;
    --text: #333333;
    --field-fill: #dedede;
    --field-border: #9a9a9a;
    --placeholder: #4caf6a;
    --white: #ffffff;
  }
  * { margin: 0; padding: 0; box-sizing: border-box; }
  html, body { width: 1200px; height: 782px; overflow: hidden; }
  body {
    position: relative;
    background: var(--page-bg);
    font-family: "Mulish", sans-serif;
    color: var(--text);
  }
  .backdrop { position: absolute; inset: 0; }
  .band {
    position: absolute; left: 0; top: 503px; width: 1200px; height: 279px;
    background: var(--brand-green);
  }

  .screen {
    position: absolute; left: 138px; top: 47px; width: 317px; height: 687px;
    background: var(--white);
    border-radius: 18px;
    overflow: hidden;
    box-shadow: 0 6px 24px rgba(0,0,0,0.08);
  }
  .app-bar {
    position: absolute; left: 0; top: 0; width: 100%; height: 85px;
    background: var(--brand-green);
    color: var(--white);
  }
  .status-time {
    position: absolute; left: 28px; top: 13px;
    font: 700 12px "Mulish", sans-serif;
  }
  .status-icons { position: absolute; right: 14px; top: 14px; }
  .back-arrow { position: absolute; left: 16px; top: 55px; }
  .app-title {
    position: absolute; left: 0; right: 0; top: 53px;
    text-align: center;
    font: 700 14px "Mulish", sans-serif;
  }

  .section-title {
    position: absolute; left: 30px;
    font-size: 13px; font-weight: 600; color: var(--text);
  }
  .intro-title { top: 112px; }
  .intro-text {
    position: absolute; left: 30px; top: 132px; width: 260px;
    font-size: 11px; line-height: 13.6px; color: var(--text);
  }
  .detail-title { top: 206px; }

  .field {
    position: absolute;
    background: var(--field-fill);
    border: 1px solid var(--field-border);
    border-radius: 3px;
    display: flex; align-items: center;
    padding-left: 21px;
    font-size: 16px; color: var(--text);
  }
  .field-station { left: 25px; top: 229px; width: 266px; height: 42px; }
  .field-location { left: 25px; top: 281px; width: 266px; height: 41px; }

  .price-label { position: absolute; top: 345px; font-size: 13px; font-weight: 600; }
  .price-label.current { left: 30px; }
  .price-label.new { left: 170px; }
  .field-current { left: 25px; top: 368px; width: 127px; height: 41px; }
  .field-new {
    left: 165px; top: 368px; width: 127px; height: 41px;
    background: var(--white); padding-left: 9px;
    font-size: 11.5px; color: var(--placeholder);
  }

  .button {
    position: absolute; left: 30px; width: 255px; height: 50px;
    border-radius: 6px;
    display: flex; align-items: center; justify-content: center;
    font-size: 13px; font-weight: 700; color: var(--white);
  }
  .button-cancel { top: 505px; background: var(--field-fill); }
  .button-save { top: 577px; background: var(--brand-green); }
  .home-indicator {
    position: absolute; left: 104px; top: 674px; width: 110px; height: 4px;
    border-radius: 2px; background: #cfcfcf;
  }

  .headline { position: absolute; left: 527px; top: 113px; font-family: "Poppins", sans-serif; }
  .headline-lead { font-size: 40px; font-weight: 500; color: var(--ink); line-height: 60px; }
  .headline-main {
    margin-top: 4px;
    font-size: 40px; font-weight: 700; color: var(--headline-green);
    line-height: 58.5px; letter-spacing: -0.3px;
  }
</style>
</head>
<body>
  <svg class="backdrop" width="1200" height="782" aria-hidden="true">
    <defs>
      <clipPath id="upper"><rect x="0" y="0" width="1200" height="503"/></clipPath>
      <clipPath id="lower"><rect x="0" y="503" width="1200" height="279"/></clipPath>
    </defs>
  </svg>
  <div class="band"></div>
  <svg class="backdrop" width="1200" height="782" aria-hidden="true">
    <circle cx="1003" cy="509" r="272" fill="var(--circle-tint)" clip-path="url(#upper)"/>
    <circle cx="1003" cy="509" r="272" fill="var(--circle-tint-dark)" clip-path="url(#lower)"/>
  </svg>

  <main class="screen">
    <header class="app-bar">
      <span class="status-time">9:41</span>
      <svg class="status-icons" width="56" height="10" viewBox="0 0 56 10" aria-hidden="true">
        <rect x="0" y="7" width="2" height="3" fill="#fff"/>
        <rect x="3" y="5" width="2" height="5" fill="#fff"/>
        <rect x="6" y="3" width="2" height="7" fill="#fff"/>
        <rect x="9" y="1" width="2" height="9" fill="#fff"/>
        <path d="M15 4 a8 8 0 0 1 11 0 M17 6 a5 5 0 0 1 7 0" stroke="#fff" stroke-width="1.4" fill="none"/>
        <circle cx="20.5" cy="8.5" r="1.2" fill="#fff"/>
        <rect x="35" y="1" width="18" height="8" rx="2" fill="none" stroke="#fff"/>
        <rect x="37" y="3" width="14" height="4" rx="1" fill="#fff"/>
        <rect x="54" y="3.5" width="1.5" height="3" fill="#fff"/>
      </svg>
      <svg class="back-arrow" width="18" height="14" viewBox="0 0 18 14" aria-hidden="true">
        <path d="M17 7H2 M7 1 L1 7 L7 13" stroke="#fff" stroke-width="1.8" fill="none" stroke-linecap="round" stroke-linejoin="round"/>
      </svg>
      <h1 class="app-title">Update Data</h1>
    </header>

    <h2 class="section-title intro-title">Update Data</h2>
    <p class="intro-text">See a difference in price? Please take a moment to update the existing data, these will help community!</p>

    <h2 class="section-title detail-title">Petrol Station Detail</h2>
    <div class="field field-station">Kestrel Fuel</div>
    <div class="field field-location">Location</div>

    <span class="price-label current">Current Price</span>
    <span class="price-label new">New Price</span>
    <div class="field field-current">₦ 225</div>
    <div class="field field-new">Enter new price here</div>

    <div class="button button-cancel">Cancel</div>
    <div class="button button-save">Save</div>
    <div class="home-indicator"></div>
  </main>

  <section class="headline">
    <p class="headline-lead">Added :</p>
    <p class="headline-main">Input Form for<br>Crowdsourced Database<br>Integration</p>
  </section>
</body>
</html>
```